Website Design for Business Law Firm

We have a logo and now we would like a web site design for our new website. Our small firm provides creative and aggressive transactional (not litigation) legal services to advise healthcare, technology, internet-based and traditional companies and investors in such companies on healthcare, technology, financing, mergers/acquisitions, real estate and other transactions, legal compliance and general corporate and business matters.

We would like to see a website design that is professional and appropriate for executives, professionals, investors and government regulators to visit, that conveys professionalism and competence while being a little edgy and modern - no typical legal motifs such as gavels, books, or scales of justice. We advise businesses and investors and guide them through complicated issues quickly, capably and differently from other law firms. We are part of the business team and get things done.

The logo is attached, and we like gray as a color to complement it. The intention of the logo is to convey that in a storm or challenging time, people come to this firm, and people come to this firm when they need the power and disruption to change things or shake them up.

I have also enclosed a picture of our business card for consideration.

On the other hand, you can check out the current simple site at www.venhollow.example to see we have used a space motif in the past to evoke that we help create stars (the nebula featured there). This is not a necessary part of the new website and it may look better without it.

We appreciate your creativity and look forward to designs.

Industry/Entity Type

Business

Requirements
Must have
• We anticipate the following pages, and you may submit different ideas for the different pages:
• 1. Landing page
• 2. Services pages - healthcare, IT/Technology, general counsel services, financings, mergers/acquisitions, mediation/arbitration, procurement and productization
• 3. About Us including contact information
• Our name and contact information:
• Quellane Law Firm, P.C.
• 8716 SW 19th Ave.
• Portland, OR 97213
• phone: 971.555.0143
• fax: 971.555.0187
Nice to have
• Please consider designs that enhance the impressions we are looking for
Should not have
• Please no gavels, scales of justice, law books, or similar traditional legal imagery.

```html
<!DOCTYPE html>
<html lang="en">
<head>
<meta charset="utf-8">
<title>Quellane Law Firm</title>
<link href="https://fonts.googleapis.com/css2?family=Bebas+Neue&family=Open+Sans:wght@400;600;700&display=swap" rel="stylesheet">
<style>
:root{
  --ink:#242424;
  --hero:#2a2a2a;
  --teal:#4f747b;
  --teal-dark:#46686f;
  --white:#ffffff;
  --muted:#8b8b8b;
  --black:#141414;
  --field:#c9c9c9;
  --text:#222222;
  --footer:#232323;
}
*{box-sizing:border-box;margin:0;padding:0}
html,body{width:1054px;height:1200px;overflow:hidden}
body{position:relative;font-family:"Open Sans",Arial,sans-serif;background:var(--white);color:var(--text)}
.abs{position:absolute}
.display{font-family:"Bebas Neue","Oswald",sans-serif;font-weight:400;letter-spacing:.5px}

/* Hero */
.hero{position:absolute;left:0;top:0;width:1054px;height:474px;background:radial-gradient(ellipse at 70% 45%,#343434 0%,var(--hero) 60%,#232323 100%)}
.hero-strip{position:absolute;left:0;top:0;width:100%;height:4px;background:var(--teal)}
.hero-rule{position:absolute;left:0;width:100%;height:1px;background:rgba(255,255,255,.06)}
.phone{position:absolute;left:726px;top:24px;display:flex;align-items:center;gap:8px;color:var(--white);font-family:"Bebas Neue",sans-serif;font-size:27px}
.phone-icon{width:22px;height:22px;border-radius:50%;background:var(--teal);display:flex;align-items:center;justify-content:center}
.nav{position:absolute;right:192px;top:66px;display:flex;gap:16px;font-family:"Bebas Neue",sans-serif;font-size:20px;letter-spacing:.3px}
.nav a{color:var(--muted);text-decoration:none}
.nav a.active{color:var(--white)}
.portrait{position:absolute;left:120px;top:12px;width:352px;height:462px;background:linear-gradient(180deg,#3a3a3a 0%,#1c1c1c 55%,#151515 100%);border-radius:140px 140px 0 0}
.brand{position:absolute;left:473px;top:138px;height:61px;display:flex;align-items:center;gap:10px;color:var(--white);font-size:40px;font-weight:600;letter-spacing:6px}
.brand-mark{width:22px;height:22px;background:var(--teal)}
.headline{position:absolute;left:478px;top:220px;color:var(--white);font-weight:700;font-size:22px;line-height:27px;letter-spacing:1.2px}
.services{position:absolute;top:286px;list-style:none;color:#dcdcdc;font-size:13px;line-height:20px}
.services li{display:flex;align-items:center;gap:6px}
.cta{position:absolute;left:473px;top:365px;width:223px;height:51px;background:var(--black);color:var(--white);font-family:"Bebas Neue",sans-serif;font-size:30px;display:flex;align-items:center;justify-content:center;letter-spacing:.5px}
.learn-link{position:absolute;left:702px;top:401px;color:#e6e6e6;font-size:11.5px;letter-spacing:1px}

/* Practices band */
.band{position:absolute;left:0;top:474px;width:1054px;height:313px;background:var(--teal)}
.band-title{position:absolute;left:190px;top:510px;color:var(--white);font-size:33px}
.band-intro{position:absolute;left:190px;top:546px;color:#eef3f4;font-size:11.5px;line-height:13px;width:290px}
.practice-photo{position:absolute;left:190px;top:582px;width:84px;height:147px;background:linear-gradient(160deg,#7d97ad 0%,#34465c 55%,#1d2835 100%);box-shadow:0 1px 3px rgba(0,0,0,.3)}
.practice-list{position:absolute;left:284px;top:582px;list-style:none;color:var(--white);font-size:10px;line-height:13.3px}
.practice-list li::before{content:"›";margin-right:3px}
.btn{position:absolute;color:var(--white);font-size:10px;display:flex;align-items:center;justify-content:center;letter-spacing:.5px}
.btn-dark{background:#2f3a3d}
.btn-teal{background:var(--teal)}

/* Contact form */
.form{position:absolute;left:499px;top:513px;width:363px;height:226px;background:var(--white)}
.form-head{position:absolute;left:24px;top:22px;display:flex;align-items:center;gap:8px;color:var(--teal);font-size:33px}
.field{position:absolute;border:1px solid var(--field);background:var(--white);color:#7a7a7a;font-size:9.5px;padding:5px 7px}
.submit{position:absolute;left:114px;top:161px;width:151px;height:39px;background:var(--ink);color:var(--white);font-family:"Bebas Neue",sans-serif;font-size:29px;display:flex;align-items:center;justify-content:center}

/* Welcome & blog */
.section-title{position:absolute;top:820px;color:var(--teal);font-size:33px}
.section-rule{position:absolute;left:192px;top:869px;width:380px;height:1px;background:#b8b8b8}
.welcome-copy{position:absolute;left:192px;top:886px;width:382px;font-size:9.8px;line-height:15.8px;color:var(--text)}
.post{position:absolute;left:607px;display:flex;gap:8px}
.post-thumb{width:44px;height:44px;flex:none}
.post-date{color:var(--teal);font-size:11.5px;line-height:13px}
.post-text{font-size:11px;line-height:12.5px;width:205px;color:var(--text)}

/* Footer */
.footer{position:absolute;left:0;top:1060px;width:1054px;height:140px;background:var(--footer);color:var(--white)}
.footer-nav{position:absolute;top:22px;left:0;width:100%;display:flex;justify-content:center;gap:14px;font-size:10px}
.footer-phone{position:absolute;top:45px;left:0;width:100%;display:flex;justify-content:center;align-items:center;gap:6px;font-size:15px}
.social{width:11px;height:11px;border-radius:50%;background:#3a8fd6}
.copyright{position:absolute;top:73px;left:0;width:100%;text-align:center;font-size:9.5px}
</style>
</head>
<body>

<header class="hero">
  <div class="hero-strip"></div>
  <div class="hero-rule" style="top:58px"></div>
  <div class="hero-rule" style="top:98px"></div>
  <div class="portrait" role="img" aria-label="Photo of a smiling young businessman in a dark suit holding a rolled newspaper"></div>

  <div class="phone">
    <span class="phone-icon"><svg width="12" height="12" viewBox="0 0 12 12"><rect x="3" y="1" width="6" height="3" fill="#fff"/><rect x="1" y="4" width="10" height="5" rx="1" fill="#fff"/><rect x="3" y="7" width="6" height="4" fill="#fff" stroke="#4f747b" stroke-width=".8"/></svg></span>
    971.555.0187
  </div>

  <nav class="nav">
    <a href="#">Home</a>
    <a href="#" class="active">Our Prectices</a>
    <a href="#">Professionals</a>
    <a href="#">Careers</a>
    <a href="#">About Us</a>
    <a href="#">Contact</a>
  </nav>

  <div class="brand"><span class="brand-mark"></span>QUELLANE</div>

  <h1 class="headline">PRAGMATIC, CREATIVE SERVICES<br>FOR INNOVATIVE BUSINESSES</h1>

  <ul class="services" style="left:478px">
    <li><svg width="10" height="10" viewBox="0 0 10 10"><circle cx="5" cy="5" r="4.2" fill="none" stroke="#ddd" stroke-width="1.2"/><path d="M3 5.2l1.5 1.4L7 3.8" fill="none" stroke="#ddd" stroke-width="1.2"/></svg>Strategic Alliances</li>
    <li><svg width="10" height="10" viewBox="0 0 10 10"><circle cx="5" cy="5" r="4.2" fill="none" stroke="#ddd" stroke-width="1.2"/><path d="M3 5.2l1.5 1.4L7 3.8" fill="none" stroke="#ddd" stroke-width="1.2"/></svg>Business Relationships</li>
    <li><svg width="10" height="10" viewBox="0 0 10 10"><circle cx="5" cy="5" r="4.2" fill="none" stroke="#ddd" stroke-width="1.2"/><path d="M3 5.2l1.5 1.4L7 3.8" fill="none" stroke="#ddd" stroke-width="1.2"/></svg>Outsourcing</li>
  </ul>
  <ul class="services" style="left:638px">
    <li><svg width="10" height="10" viewBox="0 0 10 10"><circle cx="5" cy="5" r="4.2" fill="none" stroke="#ddd" stroke-width="1.2"/><path d="M3 5.2l1.5 1.4L7 3.8" fill="none" stroke="#ddd" stroke-width="1.2"/></svg>Procurements - Buying or Selling</li>
    <li><svg width="10" height="10" viewBox="0 0 10 10"><circle cx="5" cy="5" r="4.2" fill="none" stroke="#ddd" stroke-width="1.2"/><path d="M3 5.2l1.5 1.4L7 3.8" fill="none" stroke="#ddd" stroke-width="1.2"/></svg>Licensing and Technology Exploitation</li>
    <li><svg width="10" height="10" viewBox="0 0 10 10"><circle cx="5" cy="5" r="4.2" fill="none" stroke="#ddd" stroke-width="1.2"/><path d="M3 5.2l1.5 1.4L7 3.8" fill="none" stroke="#ddd" stroke-width="1.2"/></svg>Venture Formation and Startup</li>
  </ul>

  <a class="cta">CALL TO ACTION</a>
  <span class="learn-link">Learn More &gt;&gt;</span>
</header>

<section class="band">
</section>
<h2 class="band-title display abs">OUR PRACTICES AREAS</h2>
<p class="band-intro">Lorem ipsum dolor sit amet, consectetur adipiscing elit. In fermen dolor tum dolor non augue pretium</p>
<div class="practice-photo" role="img" aria-label="Photo of a businessman giving a thumbs up"></div>
<ul class="practice-list">
  <li>Strategic Alliances</li>
  <li>Business Relationships</li>
  <li>Outsourcing</li>
  <li>Procurements - Buying or Selling</li>
  <li>Licensing and Technology Exploitation</li>
  <li>Venture Formation and Startup</li>
  <li>Venture Financing</li>
  <li>Creative Private Financing Arrangements</li>
  <li>Mergers and Acquisitions</li>
  <li>Real Estate</li>
  <li>Contacts</li>
</ul>
<a class="btn btn-dark" style="left:402px;top:725px;width:69px;height:15px">Learn More</a>

<form class="form">
  <div class="form-head display">
    <svg width="35" height="25" viewBox="0 0 35 25"><rect x="1" y="1" width="33" height="23" fill="none" stroke="#4f747b" stroke-width="2"/><path d="M1 1l16.5 13L34 1" fill="none" stroke="#4f747b" stroke-width="2"/><path d="M1 24l12-11M34 24L22 13" fill="none" stroke="#4f747b" stroke-width="2"/></svg>
    GET IN TOUCH
  </div>
  <div class="field" style="left:24px;top:69px;width:163px;height:23px">Name</div>
  <div class="field" style="left:24px;top:96px;width:163px;height:22px">Email</div>
  <div class="field" style="left:24px;top:124px;width:163px;height:21px">Phone</div>
  <div class="field" style="left:191px;top:69px;width:154px;height:76px">Comments</div>
  <div class="submit">SUBMIT</div>
</form>

<h2 class="section-title display" style="left:192px">WELCOME TO QUELLANE</h2>
<div class="section-rule"></div>
<p class="welcome-copy">Lorem ipsum dolor sit amet, consectetur adipiscing elit. In fermentum dolor non augue pretium egestas. Donec sem eros, tincidunt at congue ut, posuere sit amet est. Vivamus scelerisque viverra odio sit amet laoreet. Ut nec neque non justo rutrum tempor lobortis eu ante.&nbsp; dolor Aliquam sagittis, nibh quis commodo auctor, risus nibh mauris laoreet lectus, id facilisis libero odio nec enim. Sed id ligula adipiscing purus lacinia aliquet. Sed eu est non nisl vehicula bibendum congue sit amet enim.</p>
<a class="btn btn-teal" style="left:483px;top:1011px;width:80px;height:16px">Learn More</a>

<h2 class="section-title display" style="left:605px">BLOG AND NEWS</h2>
<article class="post" style="top:866px">
  <div class="post-thumb" role="img" aria-label="Photo of two professionals shaking hands" style="background:linear-gradient(135deg,#c9d3dc,#a24a86 60%,#e3e8ee)"></div>
  <div><div class="post-date">05 Dec, 2013</div><p class="post-text">Lorem ipsum dolor sit amet, consectetur adipiscing&nbsp; elit. In fermentum congue sit amet, consectetur...</p></div>
</article>
<article class="post" style="top:929px">
  <div class="post-thumb" role="img" aria-label="Photo of a group of business people meeting" style="background:linear-gradient(135deg,#dfe4ea,#4a5665 60%,#c5ccd4)"></div>
  <div><div class="post-date">05 Dec, 2013</div><p class="post-text">Lorem ipsum dolor sit amet, consectetur adipiscing&nbsp; elit. In fermentum congue sit amet, consectetur...</p></div>
</article>
<a class="btn btn-teal" style="left:800px;top:1011px;width:62px;height:16px">Read All</a>

<footer class="footer">
  <nav class="footer-nav"><span>Home</span><span>Our Prectices</span><span>Professionals</span><span>Careers</span><span>About us</span><span>Contact</span></nav>
  <div class="footer-phone">
    <svg width="13" height="13" viewBox="0 0 12 12"><rect x="3" y="1" width="6" height="3" fill="#fff"/><rect x="1" y="4" width="10" height="5" rx="1" fill="#fff"/><rect x="3" y="7" width="6" height="4" fill="#fff" stroke="#232323" stroke-width=".8"/></svg>
    971.555.0187
    <span class="social"></span><span class="social"></span>
  </div>
  <p class="copyright">© Copyright 2014</p>
</footer>

</body>
</html>
```